Business Card

I want our business cards to have a little more pizzazz. I like the content, and we are in healthcare (so nothing to wild or artsy), but something that allows our cards to stand out.

Business

```html
<!DOCTYPE html>
<html lang="en">
<head>
<meta charset="utf-8">
<title>Norvell Medical – Business Card</title>
<link href="https://fonts.googleapis.com/css2?family=Open+Sans:wght@400;600;700&display=swap" rel="stylesheet">
<style>
  :root {
    --page-bg: #e9ebef;
    --brand-blue: #1d4c98;
    --brand-blue-light: #2d63b3;
    --brand-blue-dark: #173f82;
    --mark-tint: rgba(160, 195, 235, 0.55);
    --ink: #2b2b2b;
    --paper: #ffffff;
    --services-text: rgba(255, 255, 255, 0.72);
    --divider: #6a78c8;
  }
  * { box-sizing: border-box; margin: 0; padding: 0; }
  html, body {
    width: 1200px; height: 900px; overflow: hidden;
    background: var(--page-bg);
    font-family: "Open Sans", Arial, sans-serif;
  }
  .canvas { position: relative; width: 1200px; height: 900px; }

  .card {
    position: absolute; left: 320px;
    width: 560px; height: 320px;
    overflow: hidden;
    box-shadow: 0 10px 28px rgba(0, 0, 0, 0.18);
  }

  /* Front face */
  .card--front {
    top: 110px;
    background: linear-gradient(100deg, var(--brand-blue-dark) 0%, var(--brand-blue) 55%, var(--brand-blue-light) 100%);
  }
  .front-mark {
    position: absolute; left: 48px; top: 62px;
    width: 190px; height: 190px;
    background: var(--mark-tint);
  }
  .services {
    position: absolute; left: 290px; top: 34px;
    list-style: none;
    color: var(--services-text);
    font-size: 14px; line-height: 17px; font-weight: 600;
  }
  .services li:nth-child(2) { padding-left: 6px; }
  .services li:nth-child(3) { padding-left: 12px; }
  .services li:nth-child(4) { padding-left: 18px; }
  .services-pointer { position: absolute; left: 312px; top: 104px; }
  .front-name {
    position: absolute; right: 34px; bottom: 62px;
    color: var(--paper);
    font-size: 38px; font-weight: 400; line-height: 1;
    letter-spacing: 0.5px;
  }

  /* Back face */
  .card--back {
    top: 470px;
    background: var(--paper);
  }
  .back-band {
    position: absolute; left: 0; top: 0; width: 100%; height: 28px;
    background: var(--brand-blue);
  }
  .brand-lockup {
    position: absolute; left: 30px; top: 178px;
    display: flex; align-items: center; gap: 10px;
  }
  .brand-square { width: 20px; height: 20px; background: var(--brand-blue); }
  .brand-name {
    color: var(--brand-blue);
    font-size: 27px; font-weight: 400; line-height: 1;
    white-space: nowrap;
  }
  .divider { position: absolute; left: 282px; top: 60px; }
  .person {
    position: absolute; left: 322px; top: 60px;
  }
  .person-name {
    color: var(--brand-blue);
    font-size: 19px; font-weight: 700; line-height: 1.2;
  }
  .person-title {
    color: var(--ink);
    font-size: 15px; line-height: 1.3;
  }
  .contacts {
    position: absolute; left: 322px; top: 150px;
    list-style: none;
    color: var(--ink); font-size: 14px; line-height: 22px;
    white-space: nowrap;
  }
  .contacts li { display: flex; align-items: center; gap: 9px; }
  .contacts svg { flex: none; }
  .contact-at { color: var(--brand-blue); font-weight: 700; width: 13px; text-align: center; }
</style>
</head>
<body>
<main class="canvas">

  <section class="card card--front" aria-label="Card front">
    <div class="front-mark" role="img" aria-label="Large faint brand mark area"></div>
    <ul class="services">
      <li>Servicing Laboratories</li>
      <li>Hospital &amp; Medical Centers</li>
      <li>Reserch Facilities</li>
      <li>Surgical Centers</li>
    </ul>
    <svg class="services-pointer" width="10" height="14" viewBox="0 0 10 14" aria-hidden="true">
      <path d="M0 0 L10 0 L2 14 Z" fill="rgba(255,255,255,0.6)"/>
    </svg>
    <p class="front-name">Norvell Medical</p>
  </section>

  <section class="card card--back" aria-label="Card back">
    <div class="back-band"></div>

    <div class="brand-lockup">
      <span class="brand-square"></span>
      <span class="brand-name">Norvell Medical</span>
    </div>

    <svg class="divider" width="26" height="150" viewBox="0 0 26 150" aria-hidden="true">
      <line x1="0" y1="0" x2="26" y2="150" stroke="var(--divider)" stroke-width="1"/>
    </svg>

    <div class="person">
      <p class="person-name">Daniel Reyes</p>
      <p class="person-title">Territory Manager</p>
    </div>

    <ul class="contacts">
      <li>
        <svg width="13" height="13" viewBox="0 0 24 24" aria-hidden="true">
          <path fill="var(--brand-blue)" d="M6.6 10.8a15.1 15.1 0 0 0 6.6 6.6l2.2-2.2c.3-.3.7-.4 1-.2 1.1.4 2.3.6 3.6.6.6 0 1 .4 1 1V20c0 .6-.4 1-1 1A17 17 0 0 1 3 4c0-.6.4-1 1-1h3.5c.6 0 1 .4 1 1 0 1.3.2 2.5.6 3.6.1.3 0 .7-.2 1z"/>
        </svg>
        <span>(555) 014-7720</span>
      </li>
      <li>
        <svg width="13" height="13" viewBox="0 0 24 24" aria-hidden="true">
          <rect x="6" y="2" width="12" height="6" fill="var(--brand-blue)"/>
          <rect x="2" y="9" width="20" height="9" rx="1" fill="var(--brand-blue)"/>
          <rect x="6" y="15" width="12" height="7" fill="var(--brand-blue)"/>
          <rect x="8" y="17" width="8" height="1.5" fill="#fff"/>
        </svg>
        <span>(555) 014-3381</span>
      </li>
      <li>
        <span class="contact-at">@</span>
        <span>d.reyes@norvellmed.com</span>
      </li>
    </ul>
  </section>

</main>
</body>
</html>
```